Luma Crest Bundle Social Media Graphics

Focusing on the Luma Crest Bundle product, create 5-6 individual social media graphics (square size). For the color scheme of the graphics, they should all be complementary with the Luma Crest Bundle bottle colors.

Note: each graphic should have one of the pictures of the bottles (2-product bundle) on it and/or one of the images with a person on it (several pics attached)/only use stock photography that I provided.

Target Market(s)

women over 40 struggling with hormonal decline

Industry/Entity Type

health and weight loss

Requirements
Nice to have
• pictures attached

```html
<!DOCTYPE html>
<html lang="en">
<head>
<meta charset="UTF-8">
<title>Luma Crest Bundle – Social Graphics</title>
<link href="https://fonts.googleapis.com/css2?family=League+Spartan:wght@500;600;700&family=Allura&family=Questrial&display=swap" rel="stylesheet">
<style>
  :root{
    --canvas:#f0f0f0;
    --white:#ffffff;
    --ink:#2c4a45;
    --teal:#5d9f95;
    --teal-mid:#6fa89f;
    --teal-deep:#2f5c55;
    --mint:#a9d6cc;
    --mint-pale:#d7ece7;
    --photo-a:#eef2f1;
    --photo-b:#d6dedc;
    --bottle:#e6ebea;
  }
  *{margin:0;padding:0;box-sizing:border-box}
  html,body{width:1200px;height:675px;overflow:hidden;background:var(--canvas)}
  .board{position:relative;width:1200px;height:675px}
  .card{position:absolute;width:291px;height:291px;overflow:hidden;font-family:"League Spartan",sans-serif}
  .card > *{position:absolute}
  .card svg.bg{left:0;top:0;width:291px;height:291px}
  .headline{color:var(--ink);font-weight:600;letter-spacing:.2px;white-space:nowrap}
  .headline .accent{color:var(--teal)}
  .headline .script{font-family:"Allura",cursive;font-weight:400;color:var(--teal);font-size:1.45em;line-height:.8;letter-spacing:0}
  .photo{border-radius:10px;background:linear-gradient(180deg,var(--photo-a),var(--photo-b))}
  .products{border-radius:10px;background:linear-gradient(90deg,var(--bottle),#fff 60%,var(--bottle))}
  .checklist{list-style:none;font-family:"Questrial",sans-serif;font-size:8.6px;color:var(--ink);white-space:nowrap}
  .checklist li{position:relative;padding-left:15px;height:18.4px;line-height:10px}
  .checklist li::before{content:"";position:absolute;left:0;top:0;width:10px;height:10px;border-radius:50%;background:var(--ink)}
  .checklist li::after{content:"";position:absolute;left:3.3px;top:2px;width:2.6px;height:4.6px;border:solid var(--white);border-width:0 1.4px 1.4px 0;transform:rotate(45deg)}
  .checklist.spaced li{height:20px}
  .checklist.light{color:var(--white)}
  .checklist.light li::before{background:var(--mint)}
  .checklist.light li::after{border-color:var(--teal-deep)}

  .card-struggling{left:132.5px;top:31px;background:var(--white)}
  .card-over40{left:454.5px;top:31px;background:linear-gradient(180deg,#fff 0%,var(--mint-pale) 55%)}
  .card-balance{left:776.5px;top:31px;background:linear-gradient(180deg,var(--mint) 0%,#fff 55%)}
  .card-accelerate{left:293.5px;top:353px;background:var(--teal-mid)}
  .card-diet{left:615.5px;top:353px;background:var(--teal-deep)}
</style>
</head>
<body>
<main class="board">

  <section class="card card-struggling">
    <div class="photo" role="img" aria-label="Smiling woman with long braids in a white tank top" style="left:170px;top:6px;width:117px;height:180px"></div>
    <svg class="bg" viewBox="0 0 291 291" aria-hidden="true">
      <path d="M0 170 Q150 160 250 291 L0 291Z" fill="var(--mint)"/>
      <path d="M0 170 Q150 160 250 291" fill="none" stroke="var(--teal)" stroke-width="2"/>
      <path d="M250 0 L291 35" stroke="var(--mint)" stroke-width="2.5"/>
      <path d="M258 0 L291 25" stroke="var(--teal)" stroke-width="2"/>
    </svg>
    <div class="headline" style="left:17px;top:14px;font-size:20.5px;line-height:25px">
      Struggling with<br><span class="accent">Hormonal</span> or<br><span class="accent">Perimenopause<br>Symptoms?</span><br>The Solution<br>is <b>HERE!</b>
    </div>
    <div class="products" role="img" aria-label="Luma Crest Bundle: capsule bottle and pump bottle" style="left:187px;top:153px;width:69px;height:119px"></div>
    <ul class="checklist" style="left:16px;top:196px">
      <li>Mood Swings</li><li>Fatigue and Low Motivation</li><li>Weight Gain; Stubborn Belly Fat</li><li>Hot Flashes &amp; Night Sweats</li><li>Brain Fog &amp; Memory Lapses</li>
    </ul>
  </section>

  <section class="card card-over40">
    <svg class="bg" viewBox="0 0 291 291" aria-hidden="true">
      <rect width="291" height="6" fill="var(--teal)"/>
      <path d="M0 190 Q145 120 291 190 L291 291 L0 291Z" fill="var(--teal)"/>
      <path d="M0 172 Q145 102 291 172" fill="none" stroke="var(--teal)" stroke-width="5"/>
      <path d="M0 45 L50 8" stroke="var(--mint)" stroke-width="2.5"/>
      <path d="M291 50 L250 8" stroke="var(--mint)" stroke-width="2.5"/>
    </svg>
    <div class="headline" style="left:0;width:291px;top:12px;text-align:center;font-size:22.5px;line-height:29px">
      Over 40 and<br>Gaining Weight Fast?<br>The <span class="script">Solution</span> is HERE!
    </div>
    <p style="left:10px;width:271px;top:104px;text-align:center;font-family:'Questrial',sans-serif;font-size:5.6px;line-height:10.5px;color:var(--ink)">Mood Swings | Fatigue and Low Motivation | Weight Gain | Stubborn Belly Fat |<br>Hot Flashes &amp; Night Sweats | Brain Fog &amp; Memory Lapses</p>
    <div class="products" role="img" aria-label="Luma Crest Bundle: capsule bottle and pump bottle" style="left:106px;top:160px;width:72px;height:122px"></div>
  </section>

  <section class="card card-balance">
    <div class="photo" role="img" aria-label="Cheerful woman in a black tank top raising both fists" style="left:152px;top:16px;width:137px;height:160px"></div>
    <svg class="bg" viewBox="0 0 291 291" aria-hidden="true">
      <path d="M0 170 Q150 140 291 200 L291 291 L0 291Z" fill="var(--teal)"/>
      <path d="M0 162 Q150 132 291 192" fill="none" stroke="var(--teal)" stroke-width="2"/>
      <path d="M255 0 L291 30" stroke="var(--teal)" stroke-width="2.5"/>
    </svg>
    <div class="headline" style="left:17px;top:12px;font-size:20.5px;line-height:27px">
      Balance Your<br><span class="script" style="font-size:1.6em">Hormones</span><br>and Feel Like<br>Yourself<br>Again!
    </div>
    <div class="products" role="img" aria-label="Luma Crest Bundle: capsule bottle and pump bottle" style="left:180px;top:145px;width:75px;height:130px"></div>
    <ul class="checklist light spaced" style="left:16px;top:188px">
      <li>Mood Swings</li><li>Fatigue and Low Motivation</li><li>Weight Gain; Stubborn Belly Fat</li><li>Hot Flashes &amp; Night Sweats</li><li>Brain Fog &amp; Memory Lapses</li>
    </ul>
  </section>

  <section class="card card-accelerate">
    <div role="img" aria-label="Faded photo of a woman with curly hair, arms open" style="left:0;top:0;width:291px;height:200px;background:radial-gradient(ellipse at 50% 40%,#82b3ab 0 25%,var(--teal-mid) 70%)"></div>
    <svg class="bg" viewBox="0 0 291 291" aria-hidden="true">
      <path d="M0 195 Q145 100 291 195 L291 291 L0 291Z" fill="var(--mint)"/>
      <path d="M0 188 Q145 92 291 188" fill="none" stroke="var(--teal-mid)" stroke-width="4"/>
      <path d="M0 30 L40 0" stroke="var(--mint)" stroke-width="2.5"/>
      <path d="M291 70 L220 0" stroke="var(--mint)" stroke-width="2"/>
    </svg>
    <div class="headline" style="left:0;width:291px;top:18px;text-align:center;font-size:19px;line-height:23px;color:var(--white)">
      Balance<br>Your Hormones to<br><span style="color:var(--ink)">Accelerate Weight Loss</span><br>and<br><span style="color:var(--ink)">Look 10 Years Younger!</span>
    </div>
    <div class="products" role="img" aria-label="Luma Crest Bundle: capsule bottle and pump bottle" style="left:46px;top:162px;width:66px;height:114px"></div>
    <ul class="checklist spaced" style="left:126px;top:176px">
      <li>Mood Swings</li><li>Fatigue and Low Motivation</li><li>Weight Gain; Stubborn Belly Fat</li><li>Hot Flashes &amp; Night Sweats</li><li>Brain Fog &amp; Memory Lapses</li>
    </ul>
  </section>

  <section class="card card-diet">
    <svg class="bg" viewBox="0 0 291 291" aria-hidden="true">
      <path d="M0 175 Q90 160 165 215 L165 291 L0 291Z" fill="var(--mint)"/>
      <path d="M0 168 Q90 152 165 208" fill="none" stroke="var(--mint)" stroke-width="2"/>
      <path d="M255 0 L291 45" stroke="var(--mint)" stroke-width="2.5"/>
      <path d="M270 0 L291 25" stroke="var(--mint)" stroke-width="2"/>
    </svg>
    <div class="photo" role="img" aria-label="Smiling woman in a white cardigan holding the two bundle bottles" style="left:196px;top:52px;width:95px;height:239px;border-radius:10px 0 0 0"></div>
    <div class="headline" style="left:16px;top:14px;font-size:22px;line-height:28.5px;color:var(--white)">
      Diet &amp; Exercise are a<br>Waste of Time<br>if Your <span class="script" style="color:var(--mint)">Hormones</span><br>are Out of<br>Balance
    </div>
    <ul class="checklist spaced" style="left:12px;top:188px">
      <li>Mood Swings</li><li>Fatigue and Low Motivation</li><li>Weight Gain; Stubborn Belly Fat</li><li>Hot Flashes &amp; Night Sweats</li><li>Brain Fog &amp; Memory Lapses</li>
    </ul>
  </section>

</main>
</body>
</html>
```